Logo, Business Card and LetterHead

Im am looking for someone to design for me Logo of my company as well as the Business Card and LetterHead

My Company is called PT. Bumi Sentosa Abadi and I do export import business.

Logo is supposed to somehow show to clients link with international trade, world or Indonesia where company is located

Industry/Entity Type

Business

Logo Text

PT. Bumi Sentosa Abadi

Logo styles of interest
Pictorial/Combination Logo
Wordmark Logo

```html
<!DOCTYPE html>
<html lang="en">
<head>
<meta charset="utf-8">
<title>PT. Bumi Sentosa Abadi – Stationery</title>
<link rel="stylesheet" href="https://fonts.googleapis.com/css2?family=Open+Sans:wght@400;600;700&family=Tinos:wght@700&display=swap">
<style>
  :root {
    --orange: #f26a21;
    --amber: #f5b21c;
    --gold: #cc8a2a;
    --cream: #f8e0a8;
    --ink: #1f1f1f;
    --paper: #ffffff;
    --sky-light: #c4f2fb;
    --sky-deep: #12d1f6;
    --sans: "Open Sans", Arial, sans-serif;
    --serif: "Tinos", "Times New Roman", serif;
  }
  * { margin: 0; padding: 0; box-sizing: border-box; }
  html, body { width: 1200px; height: 900px; overflow: hidden; }
  body {
    position: relative;
    background: linear-gradient(100deg, var(--sky-light) 0%, #6fe2f8 45%, var(--sky-deep) 100%);
    font-family: var(--sans);
  }
  address { font-style: normal; }
  .sheet { position: absolute; background: var(--paper); overflow: hidden; }
  .accent-band { position: absolute; left: 0; right: 0; }

  .mark-dot { display: block; margin: 0 auto; border-radius: 50%; background: var(--orange); }
  .mark-name { font-family: var(--serif); font-weight: 700; color: var(--orange); line-height: 1.15; }
  .company-title { position: absolute; color: var(--orange); font-weight: 700; white-space: nowrap; }

  /* Letterhead */
  .letterhead { left: 25px; top: 13px; width: 666px; height: 877px; }
  .letterhead .mark { position: absolute; left: 30px; top: 8px; width: 80px; text-align: center; }
  .letterhead .mark-dot { width: 56px; height: 56px; }
  .letterhead .mark-name { font-size: 9px; margin-top: 6px; }
  .letterhead .company-title { left: 153px; top: 20px; font-size: 33px; }
  .letterhead .band-top {
    top: 100px; height: 125px;
    background: linear-gradient(180deg, var(--orange) 0%, rgba(245,178,28,0.75) 45%, rgba(204,138,42,0.25) 80%, rgba(255,255,255,0) 100%);
  }
  .letterhead .band-bottom {
    top: 725px; bottom: 0;
    background: linear-gradient(180deg, rgba(242,106,33,0) 0%, var(--orange) 18%, var(--gold) 45%, var(--cream) 75%, var(--cream) 100%);
  }
  .letterhead .footer-info {
    position: absolute; left: 0; right: 0; bottom: 10px;
    text-align: center; font-size: 10px; color: var(--ink); line-height: 14px;
  }

  /* Business card */
  .business-card { left: 727px; top: 50px; width: 457px; height: 218px; border: 1px solid #b9b9b9; }
  .business-card .mark { position: absolute; left: 16px; top: 6px; width: 46px; text-align: center; }
  .business-card .mark-dot { width: 36px; height: 36px; }
  .business-card .mark-name { font-size: 6px; margin-top: 4px; }
  .business-card .company-title { left: 78px; top: 12px; font-size: 25px; }
  .business-card .band {
    top: 104px; bottom: 0;
    background: linear-gradient(180deg, rgba(242,106,33,0) 0%, var(--orange) 12%, var(--gold) 30%, var(--cream) 48%, var(--cream) 100%);
  }
  .holder { position: absolute; right: 36px; top: 64px; text-align: center; }
  .holder-name { font-size: 15px; font-weight: 700; color: var(--ink); line-height: 20px; }
  .holder-role { font-size: 12px; color: var(--ink); line-height: 16px; }
  .contact { position: absolute; left: 245px; top: 150px; font-size: 11px; color: var(--ink); line-height: 16px; }
  .contact .address-head { padding-left: 60px; line-height: 12px; }
  .website { position: absolute; left: 22px; top: 192px; font-size: 11px; color: var(--ink); }

  /* Logo panel */
  .logo-panel { left: 856px; top: 347px; width: 264px; height: 234px; }
  .logo-panel .mark-dot { position: absolute; left: 58px; top: 10px; width: 148px; height: 148px; }
  .logo-panel .mark-name {
    position: absolute; left: 0; right: 0; top: 156px;
    text-align: center; font-size: 19px; line-height: 28px;
  }
</style>
</head>
<body>

<section class="sheet letterhead" aria-label="Letterhead">
  <div class="accent-band band-top" role="img" aria-label="Orange and gold flowing wave band"></div>
  <div class="accent-band band-bottom" role="img" aria-label="Orange, gold and cream flowing wave band"></div>

  <div class="mark">
    <span class="mark-dot"></span>
    <p class="mark-name">PT. Bumi<br>Sentosa Abadi</p>
  </div>
  <h1 class="company-title">PT. Bumi Sentosa Abadi</h1>

  <address class="footer-info">
    Address XXX YYYYY, ZZZZZZ AAAAAAA<br>
    Tel. 123-34568 * Fax 123-45677 * www.company.com * Email: contact@compant.com
  </address>
</section>

<section class="sheet business-card" aria-label="Business card">
  <div class="accent-band band" role="img" aria-label="Orange, gold and cream flowing wave band"></div>

  <div class="mark">
    <span class="mark-dot"></span>
    <p class="mark-name">PT. Bumi<br>Sentosa Abadi</p>
  </div>
  <h2 class="company-title">PT. Bumi Sentosa Abadi</h2>

  <div class="holder">
    <p class="holder-name">Firstname M. Lastname</p>
    <p class="holder-role">Position&nbsp; XXXX</p>
  </div>

  <address class="contact">
    <p class="address-head">Address 123</p>
    <p>XXX YYY ZZZZ, AAAAAA</p>
    <p>Tel. 123-34568&nbsp; Fax 123-45677</p>
    <p>Email: contact@compant.com</p>
  </address>
  <p class="website">www.company.com</p>
</section>

<section class="sheet logo-panel" aria-label="Logo">
  <span class="mark-dot"></span>
  <p class="mark-name">PT. Bumi<br>Sentosa Abadi</p>
</section>

</body>
</html>
```